TMC Feedback sticker

We need a sticker design for our secondary school (aged 11 - 18). This is to allow teachers to provide feedback to students and vice-versa, having a conversation with the learner. I would love to have at least two different designs and it to be attractive, so that all can be included. I've attached the basic outline with the information to be presented. It should be A5 size, so that 2 of these can be fitted in.

Target Market(s)

Secondary school students

Industry/Entity Type

School

Font styles to use
Sans Serif

Requirements
Must have
• Attached details of the headings and enough space for all parties to respond.
Should not have
• Anything deemed inappropriate for secondary students

```html
<!DOCTYPE html>
<html lang="en">
<head>
<meta charset="utf-8">
<title>Formative Feedback Sticker</title>
<link rel="stylesheet" href="https://fonts.googleapis.com/css2?family=Open+Sans:wght@400;700&display=swap">
<style>
  :root {
    --bg: #e2e2e2;
    --sticker-edge: #ffffff;
    --lime: #d5dc4b;
    --red: #d9251d;
    --ink: #222222;
    --rule: #3a3a3a;
    --bubble: #ffffff;
    --bubble-shade: #6b6b6b;
  }
  html, body {
    margin: 0;
    width: 1200px;
    height: 1000px;
    overflow: hidden;
    background: var(--bg);
    font-family: "Open Sans", Arial, sans-serif;
    color: var(--ink);
  }
  .sticker {
    position: absolute;
    left: 210px;
    top: 210px;
    width: 780px;
    height: 580px;
    background: var(--sticker-edge);
    border-radius: 44px;
  }
  .sticker-face {
    position: absolute;
    inset: 16px;
    background: var(--lime);
    border-radius: 32px;
  }
  .title-tag {
    position: absolute;
    left: -4px;
    top: 38px;
    padding: 4px 14px 6px 16px;
    background: var(--red);
    color: #fff;
    font-weight: 700;
    font-size: 24px;
    line-height: 1.3;
    text-shadow: 1px 2px 2px rgba(0,0,0,0.35);
    box-shadow: 2px 3px 4px rgba(0,0,0,0.25);
    white-space: nowrap;
  }
  .teacher-code {
    position: absolute;
    left: 304px;
    top: 44px;
    font-size: 18px;
    white-space: nowrap;
  }
  .date-field {
    position: absolute;
    left: 524px;
    top: 40px;
    width: 200px;
    display: flex;
    align-items: flex-end;
    font-size: 18px;
  }
  .fill-line {
    flex: 1;
    border-bottom: 1px solid var(--rule);
    margin-left: 4px;
    margin-bottom: 5px;
  }
  .field-label {
    position: absolute;
    left: 18px;
    font-size: 15px;
    white-space: nowrap;
  }
  .rule {
    position: absolute;
    left: 10px;
    right: 18px;
    border-bottom: 1px solid var(--rule);
  }
  .tick-row {
    position: absolute;
    left: 14px;
    right: 18px;
    display: flex;
    align-items: flex-end;
    height: 20px;
  }
  .tick-row .fill-line { margin-bottom: 2px; margin-left: 4px; }
  .tick { width: 18px; height: 16px; }
  .bubbles {
    position: absolute;
    left: 0;
    top: 0;
  }
  .bubble-heading {
    position: absolute;
    font-size: 15px;
    white-space: nowrap;
  }
</style>
</head>
<body>
  <div class="sticker">
    <div class="sticker-face">
      <div class="title-tag">Formative Feedback</div>
      <div class="teacher-code">Teacher C/L or H/L</div>
      <div class="date-field">Date:<span class="fill-line"></span></div>

      <div class="field-label" style="top:108px">Strengths (What Went Well…)</div>
      <div class="rule" style="top:134px"></div>
      <div class="rule" style="top:170px"></div>

      <div class="field-label" style="top:190px">Target (Even Better If…)</div>
      <div class="rule" style="top:214px"></div>
      <div class="tick-row" style="top:226px">
        <svg class="tick" viewBox="0 0 18 16"><path d="M2 8 L7 13 L16 2" fill="none" stroke="var(--red)" stroke-width="3.5" stroke-linecap="round" stroke-linejoin="round"/></svg>
        <span class="fill-line"></span>
      </div>
      <div class="tick-row" style="top:260px">
        <svg class="tick" viewBox="0 0 18 16"><path d="M2 8 L7 13 L16 2" fill="none" stroke="var(--red)" stroke-width="3.5" stroke-linecap="round" stroke-linejoin="round"/></svg>
        <span class="fill-line"></span>
      </div>
      <div class="field-label" style="top:288px">Action</div>
      <div class="rule" style="top:326px"></div>

      <svg class="bubbles" width="748" height="548" viewBox="0 0 748 548">
        <g transform="translate(0,4)" fill="var(--bubble-shade)">
          <path d="M60 360 H332 Q362 360 362 390 V505 Q362 535 332 535 H64 Q34 535 34 505 V420 L14 372 L52 362 Z"/>
          <path d="M414 360 H690 L734 350 L716 410 V505 Q716 535 686 535 H414 Q384 535 384 505 V390 Q384 360 414 360 Z"/>
        </g>
        <g fill="var(--bubble)">
          <path d="M60 360 H332 Q362 360 362 390 V505 Q362 535 332 535 H64 Q34 535 34 505 V420 L14 372 L52 362 Z"/>
          <path d="M414 360 H690 L734 350 L716 410 V505 Q716 535 686 535 H414 Q384 535 384 505 V390 Q384 360 414 360 Z"/>
        </g>
        <g stroke="var(--rule)" stroke-width="1">
          <line x1="34" y1="410" x2="362" y2="410"/>
          <line x1="34" y1="442" x2="362" y2="442"/>
          <line x1="34" y1="474" x2="362" y2="474"/>
          <line x1="34" y1="506" x2="362" y2="506"/>
          <line x1="384" y1="400" x2="716" y2="400"/>
          <line x1="384" y1="430" x2="716" y2="430"/>
          <line x1="384" y1="460" x2="716" y2="460"/>
          <line x1="384" y1="490" x2="716" y2="490"/>
          <line x1="384" y1="520" x2="716" y2="520"/>
        </g>
      </svg>
      <div class="bubble-heading" style="left:80px; top:378px">Response (from the student):</div>
      <div class="bubble-heading" style="left:400px; top:368px">Response and reflection (from the teacher):</div>
    </div>
  </div>
</body>
</html>
```